Luxury Spa Price Brochure

We would like a 3-4 page luxury brochure created for a luxury hotel.

Here is an example of the style a layout we would like including colours: https://www.pixelvane.net/gallery/38172946/Quembrox

We would prefer a white brochure with gold trimmings and black test as a try.

Here is another example: https://www.pixelvane.net/gallery/71830452/Luxury-Yacht-Brochure

PDF of the information that needs to go in below including images.

Target Market(s)

Luxury Spa & Woman

Industry/Entity Type

Hotel

Requirements
Must have
• As per example design - identical!

```html
<!DOCTYPE html>
<html lang="en">
<head>
<meta charset="UTF-8">
<title>Spa Price List</title>
<link rel="stylesheet" href="https://fonts.googleapis.com/css2?family=Quicksand:wght@400;500;600&display=swap">
<style>
  :root {
    --page-bg: #000000;
    --gold: #b8914f;
    --ink: #f1f1f1;
  }
  html, body {
    margin: 0;
    padding: 0;
    width: 873px;
    height: 1200px;
    overflow: hidden;
    background: var(--page-bg);
  }
  .price-page {
    position: relative;
    width: 873px;
    height: 1200px;
    background: var(--page-bg);
    font-family: "Quicksand", sans-serif;
    text-transform: uppercase;
    overflow: hidden;
  }
  .corner-ornament {
    position: absolute;
    left: 0;
    width: 46px;
    height: 92px;
    background: radial-gradient(circle at 0% 50%, rgba(184,145,79,0.55), rgba(184,145,79,0) 75%);
  }
  .corner-ornament--top { top: 0; }
  .corner-ornament--bottom { top: 1106px; }
  .line {
    position: absolute;
    transform: translateY(-50%);
    white-space: nowrap;
    line-height: 1.2;
    letter-spacing: -0.02em;
  }
  .section-title {
    left: 71px;
    font-size: 17.5px;
    font-weight: 500;
    color: var(--gold);
  }
  .service {
    left: 118px;
    font-size: 14.8px;
    font-weight: 400;
    color: var(--ink);
  }
  .service--feature {
    font-size: 17px;
    font-weight: 600;
  }
  .duration {
    left: 574px;
    font-size: 17px;
    font-weight: 500;
    color: var(--gold);
  }
  .price {
    left: 750px;
    font-size: 16px;
    font-weight: 500;
    color: var(--gold);
  }
</style>
</head>
<body>
<main class="price-page">
  <div class="corner-ornament corner-ornament--top" role="img" aria-label="Gold interlocking circle ornament"></div>
  <div class="corner-ornament corner-ornament--bottom" role="img" aria-label="Gold interlocking circle ornament"></div>

  <!-- Mother-to-be -->
  <h2 class="line section-title" style="top:128px;margin:0">Mother-to-be</h2>
  <p class="line service" style="top:166px;margin:0">Radiant Mother-to-be Treatment</p>
  <p class="line duration" style="top:167px;margin:0">1hr 15mins</p>
  <p class="line price" style="top:166px;margin:0">£85</p>
  <p class="line service" style="top:199px;margin:0">New Mum Indulgence Treat</p>
  <p class="line duration" style="top:200px;margin:0">1hr 15 mins</p>
  <p class="line price" style="top:199px;margin:0">£85</p>

  <!-- Treatments -->
  <h2 class="line section-title" style="top:283px;margin:0">Treatments</h2>
  <p class="line duration" style="top:284px;margin:0">30 mins</p>
  <p class="line price" style="top:283px;margin:0">£42</p>
  <p class="line service" style="top:325px;margin:0">Tranquillity Scalp Massage</p>
  <p class="line service" style="top:362px;margin:0">Soft Feet</p>
  <p class="line service" style="top:400px;margin:0">Soft Hands</p>
  <p class="line service" style="top:433px;margin:0">Back Massage</p>

  <!-- Manicure & Pedicure -->
  <h2 class="line section-title" style="top:530px;margin:0">Lumera Manicure &amp; Pedicure</h2>
  <p class="line service" style="top:572px;margin:0">Lumera Mini Manicure / Pedicure</p>
  <p class="line duration" style="top:573px;margin:0">30mins</p>
  <p class="line price" style="top:573px;margin:0">£35</p>
  <p class="line service" style="top:609px;margin:0">Lumera Luxury Manicure / Pedicure</p>
  <p class="line duration" style="top:610px;margin:0">60mins</p>
  <p class="line price" style="top:614px;margin:0">£45 / £55</p>

  <!-- Gel polish -->
  <h2 class="line section-title" style="top:704px;margin:0">Lumera Gel Polish!</h2>
  <p class="line service" style="top:746px;margin:0">Gel Manicure / Pedicure</p>
  <p class="line duration" style="top:748px;margin:0">60mins</p>
  <p class="line price" style="top:748px;margin:0">£55</p>
  <p class="line service" style="top:783px;margin:0">Express Gel Hands/ Feet</p>
  <p class="line duration" style="top:784px;margin:0">30mins</p>
  <p class="line price" style="top:788px;margin:0">£35</p>

  <!-- Beauty essentials -->
  <h2 class="line section-title" style="top:871px;margin:0">Beauty Essentials</h2>
  <p class="line service service--feature" style="top:913px;margin:0">Everyday Beauty Essentials</p>
  <p class="line service" style="top:956px;margin:0">Eyelash Tint</p>
  <p class="line price" style="top:956px;margin:0">£15</p>
  <p class="line service" style="top:994px;margin:0">Eyebrow Tint</p>
  <p class="line price" style="top:994px;margin:0">£15</p>
  <p class="line service" style="top:1041px;margin:0">Eyelash &amp; Eyebrow Tint</p>
  <p class="line price" style="top:1041px;margin:0">£25</p>
  <p class="line service" style="top:1079px;margin:0">All About Eyes (Eyebrow Tidy-up; Tint &amp; Eyelash Tint)</p>
  <p class="line price" style="top:1079px;margin:0">£35</p>
</main>
</body>
</html>
```